Cartwell site design for e-commerce brand

I need a cartwell website for my smoking accessory brand. The name of the brand is called "RiverMoss Smoking Supplies" i need the website to have a "Sleek And modern Design" preferable with a "Black/ white Colour Scheme" . Ideally would like the site to match the packaging design of my products (see image below) if not possible will be open to other designs.
To Add need the cartwell store to be "Integrated With Pictaro and Friendvale" (@rivermosssmokingsupplies . In addition to Friendvale “rivermoss smoking supplies”) ...
Furthermore i need to be able to "Easily to upload future products" (Current only have 7 with one I’m looking to launch soon ). I will also need to be "Able to capture emails to use for email marketing in the future as the brand grows
I’m currently selling my products on quellmart, see links below;
https://www.quellmart.example/dp/X71P2KD9QA?ref=shop_item
https://www.quellmart.example/dp/X74M8NW3TB?ref=shop_item
https://www.quellmart.example/dp/X74M9RE6UC?ref=shop_item
https://www.quellmart.example/dp/X62T51HJVD?ref=shop_item
https://www.quellmart.example/dp/X62T51ZPWE?ref=shop_item
https://www.quellmart.example/dp/X62T517QXF?ref=shop_item
https://www.quellmart.example/dp/X58KWB4NYG?ref=shop_item
Target Market(s)
Cannabis / weed Smokers
Look and feel
Each slider illustrates characteristics of the customer's brand and the style your logo design should communicate.

```html
<!DOCTYPE html>
<html lang="en">
<head>
<meta charset="utf-8">
<title>RiverMoss Smoking Supplies</title>
<link href="https://fonts.googleapis.com/css2?family=Oswald:wght@500;600;700&family=Barlow:ital,wght@0,400;0,500;0,600;1,400&display=swap" rel="stylesheet">
<style>
:root{
  --ink:#1f1f1f;
  --black:#222222;
  --white:#ffffff;
  --paper:#f3f2f2;
  --grey:#666666;
  --line:#d8d8d8;
  --teal:#1d8a8f;
  --orange:#e08b2c;
  --cream:#f4e3c1;
}
*{margin:0;padding:0;box-sizing:border-box}
html,body{width:1200px;height:3264px;overflow:hidden}
body{font-family:'Barlow',sans-serif;color:var(--ink);background:var(--white);position:relative}
.head{font-family:'Oswald',sans-serif;font-weight:600;text-transform:uppercase;letter-spacing:.2px}
.btn{display:inline-block;font-family:'Oswald',sans-serif;font-weight:600;text-transform:uppercase;text-decoration:none}

.topbar{height:33px;background:var(--black);color:#ddd;font-size:13px;display:flex;align-items:center;justify-content:space-between;padding:0 112px}
.topbar span{font-size:16px}

.header{height:109px;display:flex;align-items:center;padding:0 112px;position:relative}
.brand{display:flex;flex-direction:column;line-height:1;font-family:'Oswald',sans-serif;font-weight:700;color:var(--black)}
.brand .name{font-size:44px;letter-spacing:1px}
.brand .tag{font-size:11px;letter-spacing:5px;margin-top:4px;padding-left:56px}
.nav{display:flex;gap:31px;margin-left:66px;font-family:'Oswald',sans-serif;font-weight:500;font-size:15px}
.nav a{color:var(--black);text-decoration:none}
.tools{position:absolute;right:112px;top:44px;display:flex;gap:14px}

.hero{position:relative;height:599px;overflow:hidden}
.hero-art{position:absolute;inset:0;background:linear-gradient(120deg,var(--cream) 0%,#e9b466 30%,var(--teal) 60%,#d98a35 100%)}
.hero-panel{position:absolute;left:552px;top:167px;width:648px;height:265px;background:rgba(50,45,40,.78);padding:38px 0 0 43px;color:var(--white)}
.hero-panel h1{font-size:46px;line-height:1.1}
.hero-panel p{font-size:15px;line-height:26px;margin-top:20px;width:560px;color:#eee}
.hero-panel .btn{margin-top:24px;background:var(--white);color:var(--black);font-size:16px;width:151px;height:50px;line-height:50px;text-align:center}

.welcome{height:370px;background:var(--paper);position:relative;text-align:center;overflow:hidden}
.welcome .mark{position:absolute;left:0;right:0;top:40px;font-family:'Oswald',sans-serif;font-weight:700;font-size:180px;line-height:1;color:#e6e5e5;letter-spacing:6px}
.welcome .mark-tag{position:absolute;left:0;right:0;top:258px;font-family:'Oswald',sans-serif;font-weight:700;font-size:26px;letter-spacing:22px;color:#e4e3e3}
.welcome .inner{position:relative;padding-top:85px}
.welcome h2{font-size:36px}
.welcome p{font-size:14.5px;line-height:26px;color:var(--grey);width:860px;margin:18px auto 0}
.welcome .btn{margin-top:20px;background:var(--black);color:var(--white);font-size:16px;width:144px;height:51px;line-height:51px}

.featured{height:703px;text-align:center;position:relative}
.featured h2{font-size:36px;padding-top:84px}
.featured p.lead{font-size:14.5px;line-height:26px;color:var(--grey);width:860px;margin:16px auto 0}
.featured .all{display:inline-block;margin-top:12px;font-family:'Oswald',sans-serif;font-weight:600;font-size:16px;color:var(--black);border-bottom:2px solid var(--black);line-height:20px}
.card{position:absolute;top:280px;width:232px;height:321px;border:1px solid var(--line);background:var(--white)}
.card .sale{position:absolute;left:6px;top:6px;background:var(--black);color:var(--white);font-family:'Oswald',sans-serif;font-weight:600;font-size:13px;width:66px;height:27px;line-height:27px}
.card .shot{position:absolute;left:40px;top:44px;width:152px;height:170px;background:linear-gradient(145deg,#3a3a3a,#0f0f0f);border-radius:6px}
.card h3{position:absolute;left:0;right:0;top:250px;font-size:17px}
.card .price{position:absolute;left:0;right:0;top:283px;font-size:13px;color:var(--grey)}
.promo{position:absolute;left:867px;top:280px;width:232px;height:321px;background:var(--black);color:var(--white);padding:6px}
.promo .frame{border:1px solid #888;height:100%;padding-top:18px}
.promo h3{font-size:16px;line-height:26px}
.promo p{font-size:12px;line-height:26px;padding:0 18px;margin-top:4px}
.promo .price{font-weight:600;font-size:12px;margin-top:6px}
.promo .btn{margin-top:28px;background:var(--white);color:var(--black);font-size:16px;width:126px;height:48px;line-height:48px}

.testimonials{height:483px;display:flex}
.testimonials .photo{width:600px;height:100%;background:linear-gradient(135deg,#8d9a4a 0%,#4d5a33 35%,#2b3438 60%,#1d2528 100%)}
.testimonials .copy{flex:1;background:var(--paper);padding:78px 0 0 70px}
.testimonials h2{font-size:36px}
.testimonials p{font-style:italic;font-size:14.5px;line-height:26px;color:var(--grey);width:420px;margin-top:18px;padding-left:2px}
.testimonials .btn{margin-top:36px;background:var(--black);color:var(--white);font-size:17px;width:144px;height:52px;line-height:52px;text-align:center}

.faq{height:560px;text-align:center}
.faq h2{font-size:36px;padding-top:77px}
.faq ul{list-style:none;width:696px;margin:36px auto 0;text-align:left}
.faq li{height:76px;border:1px solid var(--line);margin-bottom:-1px;display:flex;align-items:center;justify-content:space-between;padding:0 34px;font-size:16.5px;font-weight:500}
.faq li b{font-size:18px}

.footer{height:321px;background:var(--black);color:var(--white);position:relative;overflow:hidden}
.footer .ghost{position:absolute;left:420px;top:116px;font-family:'Oswald',sans-serif;font-weight:700;font-size:130px;line-height:1;color:#2a2a2a;letter-spacing:4px}
.footer .brand{position:absolute;left:112px;top:78px;color:var(--white)}
.footer .about{position:absolute;left:111px;top:166px;width:300px;font-size:14.5px;line-height:26px}
.social{position:absolute;left:111px;top:278px;display:flex;gap:15px}
.social span{width:36px;height:36px;border:2px solid var(--white);border-radius:50%}
.col{position:absolute;top:74px}
.col h4{font-size:16px}
.links{list-style:none;margin-top:18px}
.links li{font-size:16px;line-height:26px}
.links li::before,.offer p::before{content:"»";margin-right:8px}
.offer p{font-size:16px;line-height:26px;margin-top:18px;width:320px;padding-left:18px;text-indent:-18px}
.email{margin-top:20px;width:319px;height:46px;background:var(--white);display:flex;align-items:center;justify-content:space-between;padding:0 18px 0 12px;color:#555;font-size:14px}
.cards{display:flex;gap:4px;margin-top:14px}
.cards span{width:35px;height:22px;border-radius:2px;background:#5a5a5a}
.cards span:nth-child(2){background:#d9d9d9}.cards span:nth-child(3){background:#2b4ba0}.cards span:nth-child(4){background:#e9e9e9}.cards span:nth-child(5){background:#2a78c2}.cards span:nth-child(6){background:#d23b2a}
.copyright{height:86px;background:#2c2c2c;color:var(--white);font-size:13px;font-weight:600;display:flex;align-items:center;justify-content:center}
</style>
</head>
<body>

<div class="topbar"><span>‹</span>Lorem ipsum dolor sit amet, consectetur adipiscing elit, sed do eiusmod tempor incididunt<span>›</span></div>

<header class="header">
  <div class="brand"><span class="name">RIVERMOSS</span><span class="tag">SMOKING SUPPLIES</span></div>
  <nav class="nav"><a href="#">HOME</a><a href="#">ABOUT US</a><a href="#">PRODUCT</a><a href="#">REVIEWS</a><a href="#">FAQ</a><a href="#">CONTACT US</a></nav>
  <div class="tools">
    <svg width="14" height="14" viewBox="0 0 14 14"><circle cx="6" cy="6" r="4.3" fill="none" stroke="#222" stroke-width="2"/><line x1="9" y1="9" x2="13" y2="13" stroke="#222" stroke-width="2"/></svg>
    <svg width="14" height="14" viewBox="0 0 14 14"><circle cx="7" cy="4" r="3.2" fill="#222"/><path d="M1 14c0-4 3-6 6-6s6 2 6 6z" fill="#222"/></svg>
    <svg width="15" height="14" viewBox="0 0 15 14"><path d="M0 1h3l2 8h8l2-6H4" fill="none" stroke="#222" stroke-width="2"/><circle cx="6" cy="12" r="1.5" fill="#222"/><circle cx="12" cy="12" r="1.5" fill="#222"/></svg>
  </div>
</header>

<section class="hero">
  <div class="hero-art" role="img" aria-label="Retro sunburst backdrop in teal, orange and cream with a cartoon caveman mascot carrying an oversized rolled joint"></div>
  <div class="hero-panel">
    <h1 class="head">Smoking Supplies Specialise</h1>
    <p>Lorem ipsum dolor sit amet, consectetur adipiscing elit, sed do eiusmod tempor incididunt ut labore et dolore magna aliqua.</p>
    <a class="btn" href="#">Get Started</a>
  </div>
</section>

<section class="welcome">
  <div class="mark" aria-hidden="true">RIVERMOSS</div>
  <div class="mark-tag" aria-hidden="true">SMOKING SUPPLIES</div>
  <div class="inner">
    <h2 class="head">Welcome to RiverMoss Smoking</h2>
    <p>Lorem ipsum dolor sit amet, consectetur adipiscing elit, sed do eiusmod tempor incididunt ut labore et dolore magna aliqua. Ut enim ad minim veniam, quis nostrud exercitation ullamco commodo consequat.</p>
    <a class="btn" href="#">Learn More</a>
  </div>
</section>

<section class="featured">
  <h2 class="head">Our Featured Products</h2>
  <p class="lead">Lorem ipsum dolor sit amet, consectetur adipiscing elit, sed do eiusmod tempor incididunt ut labore et dolore magna aliqua. Ut enim ad minim veniam, quis nostrud exercitation ullamco commodo consequat.</p>
  <a class="all" href="#">VIEW ALL PRODUCTS</a>

  <div class="card" style="left:123px"><span class="sale">SALE</span><div class="shot" role="img" aria-label="Black UV storage stash jar beside its box"></div><h3 class="head">UV Storage Stash Jar</h3><div class="price">$ 120:00</div></div>
  <div class="card" style="left:370px"><span class="sale">SALE</span><div class="shot" role="img" aria-label="Black smell proof bags fanned out"></div><h3 class="head">Smell Proof Bag</h3><div class="price">$ 120:00</div></div>
  <div class="card" style="left:618px"><span class="sale">SALE</span><div class="shot" role="img" aria-label="Black herb grinder set with its box"></div><h3 class="head">Herb Grinder Set</h3><div class="price">$ 120:00</div></div>
  <div class="promo"><div class="frame">
    <h3 class="head">Today One<br>Shop Our Newest Sale</h3>
    <p>Lorem ipsum dolor sit amet, consectetur adipiscing elit, sed do eiusmod tempor incididunt</p>
    <div class="price">$ 120:00</div>
    <a class="btn" href="#">Shop Now</a>
  </div></div>
</section>

<section class="testimonials">
  <div class="photo" role="img" aria-label="Dried cannabis buds on a dark surface with a black grinder and box"></div>
  <div class="copy">
    <h2 class="head">Cleint Testimonials</h2>
    <p>"Lorem ipsum dolor sit amet, consectetur adipiscing elit, sed do eiusmod tempor incididunt ut labore et dolore magna aliqua. Ut enim ad minim veniam, quis nostrud exercitation ullamco laboris nisi ut aliquip ex ea commodo consequat. Duis aute irure dolor in reprehenderit in voluptate velit esse cillum dolore eu fugiat nulla pariatur. Excepteur sint occaecat cupidatat non proident, sunt in culpa qui officia deserunt mollit anim id est laborum."</p>
    <a class="btn" href="#">View More</a>
  </div>
</section>

<section class="faq">
  <h2 class="head">Frequently Asked Questions (FAQ)</h2>
  <ul>
    <li>Lorem ipsum dolor sit amet, consectetur adipiscing elit ?<b>+</b></li>
    <li>Lorem ipsum dolor sit amet, consectetur adipiscing elit ?<b>+</b></li>
    <li>Lorem ipsum dolor sit amet, consectetur adipiscing elit ?<b>+</b></li>
    <li>Lorem ipsum dolor sit amet, consectetur adipiscing elit ?<b>+</b></li>
  </ul>
</section>

<footer class="footer">
  <div class="ghost" aria-hidden="true">RIVERMOSS</div>
  <div class="brand"><span class="name">RIVERMOSS</span><span class="tag">SMOKING SUPPLIES</span></div>
  <p class="about">sit voluptatem accusantium doloremque laudantium, totam rem aperiam, eaque ipsa quae ab illo inventore veritatis et</p>
  <div class="social" aria-label="Social links"><span></span><span></span><span></span><span></span><span></span><span></span></div>

  <div class="col" style="left:533px">
    <h4 class="head">Quick Links</h4>
    <ul class="links"><li>Home</li><li>About Us</li><li>Product</li><li>Reviews</li><li>FAQ</li><li>Contact Us</li><li>FeedBack</li></ul>
  </div>
  <div class="col offer" style="left:768px">
    <h4 class="head">Introduce an Email Offer</h4>
    <p>dicta sunt explicabo. Nemo enim ipsam voluptatem quia voluptas sit</p>
    <div class="email">Enter The email
      <svg width="18" height="16" viewBox="0 0 18 16"><path d="M0 7L18 0 14 16 9 11 15 3 7 10z" fill="#222"/></svg>
    </div>
    <div class="cards" aria-label="Accepted payment methods"><span></span><span></span><span></span><span></span><span></span><span></span></div>
  </div>
</footer>

<div class="copyright">© Copyrights 2021 RiverMoss Smoking Supplies &nbsp; | &nbsp; All Rights Reserved</div>

</body>
</html>
```